Business Card for premium dental clinic

We are a premium dental clinic based in Brasov, Romania with more than 15 year on the market, providing quality dental treatment made by a team of more specialized dentists, working with modern equipment as a solution to beautiful and healthy teeth.

Our current logo for the clinic use 2 square with colors black and gold - dr Corbescu - studio, using family fonts Bodoni, Myriad Pro and Segoe Print.
Depending on the printing we used some gold CMYK background or gold foil picture background or a gold gradient.
We want a business card:
- eye catching business card
- distinguished business card
- premium design
- to keep the color scheme of black and gold
- to attract the customers to spent time reading the information
- modern concept

```html
<!DOCTYPE html>
<html lang="en">
<head>
<meta charset="utf-8">
<title>dr Corbescu studio – business card</title>
<link rel="stylesheet" href="https://fonts.googleapis.com/css2?family=Roboto+Condensed:wght@300;400&family=Roboto:wght@400;500;700&display=swap">
<style>
  :root {
    --backdrop: #e8e8e8;
    --paper: #f7f7f5;
    --ink: #1a1a1a;
    --ink-soft: #3c3c3c;
    --black: #050505;
    --gold: #e2a92a;
    --gold-light: #f6d66a;
    --gold-deep: #b9841a;
    --rule: #6a6a6a;
  }
  * { box-sizing: border-box; margin: 0; padding: 0; }
  html, body { width: 1200px; height: 1069px; overflow: hidden; }
  body {
    background: var(--backdrop);
    font-family: "Roboto", sans-serif;
    color: var(--ink);
    position: relative;
  }
  .card {
    position: absolute;
    left: 220px;
    width: 760px;
    height: 430px;
    background: var(--paper);
    overflow: hidden;
    box-shadow: 0 6px 18px rgba(0,0,0,0.12);
  }
  .card--front { top: 75px; }
  .card--back { top: 565px; }

  /* Front */
  .front__foil {
    position: absolute; left: 0; top: 0;
    width: 390px; height: 360px;
    background: radial-gradient(circle at 35% 40%, var(--gold-light), var(--gold) 45%, var(--gold-deep) 100%);
  }
  .front__panel {
    position: absolute; left: 390px; top: 0;
    width: 370px; height: 360px;
    background: var(--black);
    display: flex; flex-direction: column; justify-content: center;
    padding: 0 40px;
  }
  .front__name {
    font-family: "Roboto Condensed", sans-serif;
    font-weight: 300;
    color: #ffffff;
    font-size: 58px;
    line-height: 1.05;
  }
  .front__url {
    position: absolute; left: 0; bottom: 0;
    width: 760px; height: 70px;
    display: flex; align-items: center; justify-content: center;
    font-size: 17px;
    letter-spacing: 17px;
    color: var(--ink);
  }

  /* Back */
  .back__brand {
    position: absolute; right: 40px; top: 40px;
    display: flex; align-items: center; gap: 12px;
  }
  .back__brand-square { width: 22px; height: 22px; background: var(--gold); }
  .back__brand-name {
    font-family: "Roboto Condensed", sans-serif;
    font-weight: 400;
    font-size: 26px;
    color: var(--ink);
  }
  .back__rule {
    position: absolute; left: 200px; right: 40px; top: 250px;
    height: 1px; background: var(--rule);
  }
  .person {
    position: absolute; left: 40px; top: 228px;
  }
  .person__name { font-weight: 700; font-size: 26px; color: var(--gold); }
  .person__role { font-weight: 500; font-size: 16px; color: var(--ink); margin-top: 2px; }
  .contacts {
    position: absolute; left: 44px; top: 305px;
    list-style: none;
    font-size: 17px; color: var(--ink-soft);
  }
  .contacts li { display: flex; align-items: center; gap: 12px; height: 26px; }
  .contacts svg { width: 15px; height: 15px; fill: var(--gold); flex: none; }
  .address {
    position: absolute; right: 40px; top: 268px;
    text-align: right;
    font-size: 17px; line-height: 1.45; color: var(--ink-soft);
  }
  .address__url { color: var(--gold); margin-top: 4px; }
</style>
</head>
<body>

<section class="card card--front">
  <div class="front__foil" role="img" aria-label="Crumpled gold foil texture"></div>
  <div class="front__panel">
    <p class="front__name">dr Corbescu<br>studio</p>
  </div>
  <p class="front__url">www.corbescustudio.com</p>
</section>

<section class="card card--back">
  <div class="back__brand">
    <span class="back__brand-square"></span>
    <span class="back__brand-name">dr Corbescu studio</span>
  </div>

  <div class="back__rule"></div>

  <div class="person">
    <p class="person__name">Radu Ionescu</p>
    <p class="person__role">President</p>
  </div>

  <ul class="contacts">
    <li>
      <svg viewBox="0 0 16 16" aria-hidden="true"><path d="M3.6 1.2l2.3 2.6-1.2 1.7c.9 2 2.7 3.8 4.8 4.8l1.7-1.2 2.6 2.3-1.4 2.4C7.5 13.6 2.4 8.5 1.2 3z"/></svg>
      268-410-2205
    </li>
    <li>
      <svg viewBox="0 0 16 16" aria-hidden="true"><path d="M4 1h8v14H4zM5.5 2.5v10h5v-10z"/></svg>
      268-734-1190
    </li>
    <li>
      <svg viewBox="0 0 16 16" aria-hidden="true"><path d="M4 1h7v4H4zM1 6h14v7h-3v2H4v-2H1zM5 11v3h6v-3z"/></svg>
      268-410-2206
    </li>
    <li>
      <svg viewBox="0 0 16 16" aria-hidden="true"><path d="M1 3h14v10H1zM2.5 4.5L8 9l5.5-4.5z"/></svg>
      hello@corbescustudio.com
    </li>
  </ul>

  <div class="address">
    <p>14 Linden Street</p>
    <p>Brasov, Romania 500123</p>
    <p class="address__url">www.corbescustudio.com</p>
  </div>
</section>

</body>
</html>
```